Commercial Flyer- For Commercial Inspection Company

Hello our commercial division needs a flyer that represents our services. Our Website is harborlinesurvey.com.
Ther Front Side will look somewhat like the chatgpt image attached.
The Back side will go more into depth on each of the categories.
Required Balcony and Deck inspections: Insurance inspections: Lender requirement inspections: Roof Certifications: Foundation Inspections: HOA inspections: Multi-unit common area inspections: Mold Inspections

Harborline Survey Commercial Inspections
Comprehensive Services for California Property Owners & Managers
✅ Specialized Inspection Services
Required Balcony and Deck Inspections (SB326/SB721 Compliant)
California law requires routine balcony and deck inspections for multi-family residential buildings to prevent accidents and liability.
We offer certified inspections that meet all SB721 (rental properties) and SB326 (HOA properties) requirements, with detailed reporting for compliance and peace of mind.

Insurance Inspections
Insurance carriers often mandate property condition reports before issuing or renewing coverage.
Our inspections document current property condition and identify risks — helping you secure favorable insurance terms and avoid unexpected policy cancellations.

Lender Requirement Inspections
Lenders demand clear evidence of property condition before funding.
Our thorough assessments meet California lender standards, addressing structural integrity, building systems, and deferred maintenance concerns to streamline financing approval.

Roof Certifications
A well-maintained roof is essential for insurance, lenders, and buyers.
Our licensed roof inspections provide 2–5 year certifications (where applicable), verifying roof integrity and ensuring compliance with California’s stringent building codes.

Foundation Inspections
California’s soils and seismic risks make foundation evaluations critical.
We visually assess for settlement, cracks, moisture intrusion, and structural concerns. Advanced recommendations are made when necessary to mitigate costly future repairs.

HOA Inspections
California HOAs have increasing responsibility to ensure safety and compliance.
We help HOA boards inspect common areas, structural components, and building exteriors — reducing liability and supporting accurate budget reserves and maintenance plans.

Multi-unit Common Area Inspections
From apartments to condo communities, we inspect shared spaces to ensure safety and compliance with California code and insurance requirements.
We cover hallways, parking, stairwells, exteriors, and more — ideal for HOA Boards, property managers, and investors.

Mold Inspections
Mold risks are heightened in California’s coastal and mixed-climate regions.
We offer mold sampling (air and surface), moisture evaluations, and expert reporting — preventing costly remediation and protecting tenant health.

🚨 Protect Your Investment — Minimize Risk
Harborline Survey has been California’s leader in inspections for over 35 years. Our certified team delivers fast, detailed reports that help:

✔️ Prevent lawsuits and code violations
✔️ Meet legal requirements (SB326/SB721)
✔️ Satisfy lenders, insurers, and HOAs
✔️ Avoid deferred maintenance disasters

📲 Schedule Your Inspection Today
HarborlineSurveyCommercial.com
(Phone Number) | (Email Address)
Serving Commercial Clients Throughout California

Target Market(s)

Commercial Real Estate Agents and Clients

Industry/Entity Type

Real Estate

Requirements
Must have
• Branding- Red and Blue

```html
<!DOCTYPE html>
<html lang="en">
<head>
<meta charset="utf-8">
<title>Harborline Survey – Commercial Division Flyer</title>
<link href="https://fonts.googleapis.com/css2?family=Roboto:wght@400;500;700;900&family=Roboto+Condensed:wght@400;700&display=swap" rel="stylesheet">
<style>
:root{
  --red:#e31d32;
  --red-dark:#b8111f;
  --navy:#0f2a6b;
  --blue:#1550a8;
  --sky:#cfe0f5;
  --ink:#1d1d1f;
  --grey:#f1f1f1;
  --white:#ffffff;
}
*{box-sizing:border-box;margin:0;padding:0}
html,body{width:810px;height:1200px;overflow:hidden}
body{background:#ececec;font-family:'Roboto',sans-serif;color:var(--ink);position:relative}
.page{position:absolute;left:180px;width:450px;height:582px;background:var(--white);overflow:hidden;box-shadow:0 2px 8px rgba(0,0,0,.15)}
.front{top:12px}
.back{top:606px}
.abs{position:absolute}

/* front */
.hero-photo{left:0;top:0;width:450px;height:208px;background:linear-gradient(100deg,#8d8f96 0%,#c9ced6 30%,#a9c6ea 55%,#d7e5f6 100%)}
.corner-stripes{left:0;top:0}
.title-box{left:88px;top:54px;width:269px;height:153px;background:linear-gradient(180deg,var(--red) 0%,var(--red-dark) 100%);color:var(--white);text-align:center;padding-top:6px}
.title-box h1{font-weight:900;font-size:37px;line-height:38px;letter-spacing:.5px}
.title-box h1 .star{font-size:14px;vertical-align:middle}
.title-box .sub{font-family:'Roboto',sans-serif;font-weight:300;font-size:15px;letter-spacing:1.2px;margin-top:8px;border-top:1px solid rgba(255,255,255,.5);border-bottom:1px solid rgba(255,255,255,.5);display:inline-block;padding:2px 6px}
.title-box .tag{font-size:16px;font-weight:500;margin-top:8px;display:flex;align-items:center;justify-content:center;gap:6px}
.logo-box{left:371px;top:0;width:79px;height:54px;background:var(--white);display:flex;flex-direction:column;align-items:center;justify-content:center;gap:3px}
.logo-box .mark{width:22px;height:22px;border-radius:50%;background:var(--red)}
.logo-box .name{font-size:7px;font-weight:700;color:var(--navy);text-align:center;line-height:8px}
.services-tab{left:12px;top:232px;height:21px;width:104px;background:var(--navy);color:var(--white);font-size:13px;padding:2px 10px}
.services-rule{left:12px;top:252px;width:426px;height:1px;background:var(--navy)}
.tile{width:96px}
.tile .ph{width:96px;height:56px;position:relative}
.tile .ph::after{content:"";position:absolute;right:0;top:0;border-top:12px solid var(--red);border-left:12px solid transparent}
.tile .cap{font-size:8.5px;line-height:9.5px;margin-top:4px}
.ph.brick{background:linear-gradient(160deg,#bcd3ec,#b0734f 60%,#8a8a82)}
.ph.concrete{background:linear-gradient(160deg,#e2e8ef,#c9cfd6 55%,#8fb27a)}
.ph.apartment{background:linear-gradient(160deg,#dfe4ea,#707780 50%,#cfd4d9)}
.ph.industrial{background:linear-gradient(160deg,#c7d2de,#8e4c34 55%,#6c6c6c)}
.ph.office{background:linear-gradient(160deg,#aac8ee,#6f8fb4 55%,#d9e1ea)}
.ph.restaurant{background:linear-gradient(160deg,#a8c4e8,#b3553f 50%,#5b5b5b)}
.ph.station{background:linear-gradient(160deg,#9fc0e6,#d8b03a 45%,#b32b27 70%,#777)}
.ph.inspect{background:linear-gradient(160deg,#e7e7e7,#8b8b8b 55%,#4a4a4a)}
.ph.roof{background:linear-gradient(160deg,#c7d1dc,#e9ecef 60%,#9aa3ad)}
.since-band{left:60px;top:528px;width:323px;height:18px;background:var(--red);color:var(--white);font-size:12px;text-align:center;letter-spacing:.6px;line-height:18px}
.since-band b{font-style:italic}
.footer-grey{left:0;top:553px;width:450px;height:29px;background:var(--grey)}
.phone-box{left:0;top:553px;width:223px;height:29px;background:var(--navy);color:var(--white);font-size:18px;display:flex;align-items:center;gap:10px;padding-left:14px}
.contact-lines{left:232px;top:557px;font-size:6.5px;line-height:10px;color:var(--ink)}
.contact-lines div{display:flex;align-items:center;gap:4px}

/* back */
.head-band{left:0;top:0}
.head-title{left:0;top:8px;width:450px;text-align:center;color:var(--white);font-weight:700;font-size:22px;line-height:28px}
.head-title .star{font-size:15px}
.sub-box{left:88px;top:92px;width:275px;height:46px;background:var(--navy);color:var(--white);text-align:center;font-size:14px;line-height:18px;padding-top:5px;font-weight:400}
.sub-box b{font-weight:700}
.right-wash{left:226px;top:150px;width:224px;height:308px;background:linear-gradient(90deg,#ffffff 0%,#e3eefb 100%)}
.item{width:212px}
.item .hd{display:flex;align-items:flex-start;gap:4px}
.item .num{background:var(--red);color:var(--white);font-size:8px;width:13px;height:18px;display:flex;align-items:center;justify-content:center;flex:none;margin-top:1px}
.item h3{font-weight:500;font-size:12px;line-height:12.5px;color:var(--navy)}
.item p{font-size:6px;line-height:7.3px;margin-top:6px}
.protect{left:0;top:458px;width:226px;height:124px;background:linear-gradient(180deg,var(--blue),var(--navy));color:var(--white);padding:12px 12px}
.protect h2{font-weight:400;font-size:14px}
.protect h2 b{font-weight:700}
.protect .min{font-size:9px;margin-top:1px}
.protect ul{list-style:none;margin-top:10px;padding-left:14px}
.protect li{font-size:6.5px;line-height:15px}
.schedule{left:226px;top:458px;width:224px;height:124px;background:var(--white);padding:18px 14px}
.schedule .cta{font-size:11px}
.schedule .cta b{color:var(--red);font-size:16px;font-weight:700}
.schedule .ph-line{display:flex;align-items:center;gap:8px;color:var(--red);font-weight:700;font-size:20px;margin-top:4px}
.schedule .mail{display:flex;align-items:center;gap:5px;font-size:10px;color:var(--navy);margin-top:3px}
.schedule .ribbon{margin-top:6px;background:var(--red);color:var(--white);font-size:7px;padding:4px 8px;display:inline-block}
.blue-top{left:0;top:456px;width:450px;height:3px;background:var(--blue)}
</style>
</head>
<body>

<section class="page front" aria-label="Flyer front">
  <div class="abs hero-photo" role="img" aria-label="Photo of a modern multi-storey apartment building with balconies under a blue sky"></div>
  <svg class="abs corner-stripes" width="450" height="240" viewBox="0 0 450 240" aria-hidden="true">
    <polygon points="0,0 44,0 0,44" fill="#e31d32"/>
    <polygon points="50,0 60,0 0,60 0,50" fill="#ffffff"/>
    <polygon points="0,186 88,196 88,201 0,191" fill="#e31d32"/>
    <polygon points="0,197 88,206 0,206" fill="#ffffff"/>
    <polygon points="357,186 450,170 450,176 357,192" fill="#e31d32"/>
    <polygon points="357,196 450,182 450,188 357,202" fill="#e31d32"/>
  </svg>
  <div class="abs title-box">
    <h1>Commercial<br><span class="star">★★</span>Division<span class="star">★★</span></h1>
    <div class="sub">Large or Small- New or Older</div>
    <div class="tag">
      <svg width="18" height="16" viewBox="0 0 18 16" aria-hidden="true"><rect x="2" y="3" width="9" height="12" fill="none" stroke="#fff" stroke-width="1.3"/><rect x="11" y="8" width="5" height="7" fill="none" stroke="#fff" stroke-width="1.3"/><line x1="4" y1="6" x2="9" y2="6" stroke="#fff"/><line x1="4" y1="9" x2="9" y2="9" stroke="#fff"/></svg>
      Balcony Inspections
    </div>
  </div>
  <div class="abs logo-box"><span class="mark"></span><span class="name">Harborline Survey</span></div>

  <div class="abs services-tab">Our Services</div>
  <div class="abs services-rule"></div>

  <div class="abs tile" style="left:12px;top:262px"><div class="ph brick" role="img" aria-label="Photo of a retail strip centre"></div><div class="cap">Retail Strip Centre</div></div>
  <div class="abs tile" style="left:121px;top:262px"><div class="ph concrete" role="img" aria-label="Photo of a concrete tilt-up warehouse"></div><div class="cap">Concrete Tilt-up<br>Warehouse</div></div>
  <div class="abs tile" style="left:230px;top:262px"><div class="ph apartment" role="img" aria-label="Photo of apartment buildings"></div><div class="cap">Appartment Buildings</div></div>
  <div class="abs tile" style="left:339px;top:262px"><div class="ph industrial" role="img" aria-label="Photo of an industrial brick building"></div><div class="cap">Industrial Buildings</div></div>

  <div class="abs tile" style="left:12px;top:359px"><div class="ph office" role="img" aria-label="Photo of an office building"></div><div class="cap">Office Buildings</div></div>
  <div class="abs tile" style="left:121px;top:359px"><div class="ph restaurant" role="img" aria-label="Photo of a restaurant building"></div><div class="cap">Restaurants</div></div>
  <div class="abs tile" style="left:230px;top:359px"><div class="ph office" role="img" aria-label="Photo of a hotel building"></div><div class="cap">Hotels &amp; Motels</div></div>
  <div class="abs tile" style="left:339px;top:359px"><div class="ph office" role="img" aria-label="Photo of a church building"></div><div class="cap">Churches</div></div>

  <div class="abs tile" style="left:12px;top:444px"><div class="ph station" role="img" aria-label="Photo of a gas station"></div><div class="cap">Gas Stations</div></div>
  <div class="abs tile" style="left:121px;top:444px"><div class="ph inspect" role="img" aria-label="Photo of an inspector at work"></div><div class="cap">Lore Ipsum</div></div>
  <div class="abs tile" style="left:230px;top:444px"><div class="ph inspect" role="img" aria-label="Photo of an inspector checking a wall"></div><div class="cap">Lore Ipsum</div></div>
  <div class="abs tile" style="left:339px;top:444px"><div class="ph roof" role="img" aria-label="Photo of an inspector on a flat roof"></div><div class="cap">Lore Ipsum</div></div>

  <div class="abs since-band">Inspecting Commercial buildings Since <b>1984</b></div>
  <div class="abs footer-grey"></div>
  <div class="abs phone-box">
    <svg width="14" height="14" viewBox="0 0 14 14" aria-hidden="true"><rect width="14" height="14" rx="2" fill="#fff"/><path d="M4 3.2l1.6-.2 1 2.2-1 .8c.5 1.1 1.3 1.9 2.4 2.4l.8-1 2.2 1-.2 1.6c-4 .3-7.1-2.8-6.8-6.8z" fill="#0f2a6b"/></svg>
    1-800-555-0147
  </div>
  <div class="abs contact-lines">
    <div><svg width="7" height="6" viewBox="0 0 7 6" aria-hidden="true"><rect x=".5" y=".5" width="6" height="5" fill="none" stroke="#e31d32"/><path d="M.5 .5l3 2.5 3-2.5" fill="none" stroke="#e31d32"/></svg>commercial@harborlinesurvey.com</div>
    <div><svg width="6" height="8" viewBox="0 0 6 8" aria-hidden="true"><path d="M3 8C1 5 0 4 0 3a3 3 0 016 0c0 1-1 2-3 5z" fill="#e31d32"/></svg>2150 Marina Vista Drive #310 Oakland CA 94607</div>
  </div>
</section>

<section class="page back" aria-label="Flyer back">
  <svg class="abs head-band" width="450" height="90" viewBox="0 0 450 90" aria-hidden="true">
    <polygon points="0,0 450,0 450,64 0,72" fill="#e31d32"/>
    <polygon points="0,0 34,0 0,32" fill="#ffffff"/>
    <polygon points="0,76 450,68 450,72 0,80" fill="#0f2a6b"/>
  </svg>
  <div class="abs head-title">Specialized Inspection<br><span class="star">★★</span> Services <span class="star">★★</span></div>
  <div class="abs sub-box">Comprehensive <b>Services</b> for California<br>Property Owners &amp; Managers</div>
  <div class="abs right-wash"></div>

  <div class="abs item" style="left:12px;top:152px">
    <div class="hd"><span class="num">01</span><h3>Specialized Inspection<br>Services</h3></div>
    <p>Required Balcony and Deck Inspections (SB326/SB721 Compliant)<br>California law requires routine balcony and deck inspections for multi-family residential buildings to prevent accidents and liability.<br>We offer certified inspections that meet all SB721 (rental properties) and SB326 (HOA properties) requirements, with detailed reporting for compliance and peace of mind.</p>
  </div>
  <div class="abs item" style="left:12px;top:266px">
    <div class="hd"><span class="num">02</span><h3>Lender Requirement<br>Inspections</h3></div>
    <p>Lenders demand clear evidence of property condition before funding.<br>Our thorough assessments meet California lender standards, addressing structural integrity, building systems, and deferred maintenance concerns to streamline financing approval.</p>
  </div>
  <div class="abs item" style="left:12px;top:364px">
    <div class="hd"><span class="num">03</span><h3>Roof<br>Certifications</h3></div>
    <p>A well-maintained roof is essential for insurance, lenders, and buyers.<br>Our licensed roof inspections provide 2–5 year certifications (where applicable), verifying roof integrity and ensuring compliance with California's stringent building codes.</p>
  </div>
  <div class="abs item" style="left:241px;top:152px">
    <div class="hd"><span class="num">04</span><h3>Insurance<br>Inspections</h3></div>
    <p>Insurance carriers often mandate property condition reports before issuing or renewing coverage.<br>Our inspections document current property condition and identify risks — helping you secure favorable insurance terms and avoid unexpected policy cancellations.</p>
  </div>
  <div class="abs item" style="left:241px;top:245px">
    <div class="hd"><span class="num">05</span><h3>Foundation<br>Inspections</h3></div>
    <p>California's soils and seismic risks make foundation evaluations critical.<br>We visually assess for settlement, cracks, moisture intrusion, and structural concerns. Advanced recommendations are made when necessary to mitigate costly future repairs.</p>
  </div>
  <div class="abs item" style="left:241px;top:341px">
    <div class="hd"><span class="num">06</span><h3>HOA<br>Inspections</h3></div>
    <p>California HOAs have increasing responsibility to ensure safety and compliance.<br>We help HOA boards inspect common areas, structural components, and building exteriors — reducing liability and supporting accurate budget reserves and maintenance plans.</p>
  </div>

  <div class="abs blue-top"></div>
  <div class="abs protect">
    <h2>Protect Your <b>Investment</b></h2>
    <div class="min">– Minimize Risk</div>
    <ul>
      <li>Prevent lawsuits and code violations</li>
      <li>Meet legal requirements (SB326/SB721)</li>
      <li>Satisfy lenders, insurers, and HOAs</li>
      <li>Avoid deferred maintenance disasters</li>
    </ul>
  </div>
  <div class="abs schedule">
    <div class="cta">Schedule Your Inspection <b>Today</b></div>
    <div class="ph-line">
      <svg width="15" height="15" viewBox="0 0 14 14" aria-hidden="true"><rect width="14" height="14" rx="2" fill="#0f2a6b"/><path d="M4 3.2l1.6-.2 1 2.2-1 .8c.5 1.1 1.3 1.9 2.4 2.4l.8-1 2.2 1-.2 1.6c-4 .3-7.1-2.8-6.8-6.8z" fill="#fff"/></svg>
      1-800-555-0147
    </div>
    <div class="mail"><svg width="8" height="7" viewBox="0 0 7 6" aria-hidden="true"><rect x=".5" y=".5" width="6" height="5" fill="#e31d32"/><path d="M.5 .5l3 2.5 3-2.5" fill="none" stroke="#fff" stroke-width=".6"/></svg>commercial@harborlinesurvey.com</div>
    <div class="ribbon">Serving Commercial Clients Throughout California</div>
  </div>
</section>

</body>
</html>
```